innovative investment real estate sales firm

We are a uniquely collabrative firm that seeks to bring a conultative approach to uncovering hidden opportunities for our clients, our website needs to convey our client focused approach. Our firm specializes in the sale of apartment properties in Southern California. We have a team of researchers, transaction coordinators and marketing personal to support our geographically specialized advisers. We need a website that introduces clients to our unique way of better helping them achieve their investment goals.

Target Market(s)

High net worth individuals and families

Industry/Entity Type

Real Estate Agent

Font styles to use
Other font styles liked:
• please use font provided

Requirements
Must have
• Stories of our recent projects
• Features on our people
• email capture for viewing inventory
• content that showcases our unique consultative approach that uncovers unrealized opportunities

```html
<!DOCTYPE html>
<html lang="en">
<head>
<meta charset="utf-8">
<title>Meridian Advisers — Multifamily Properties</title>
<link href="https://fonts.googleapis.com/css2?family=Montserrat:wght@400;600;700&family=Open+Sans:ital,wght@0,400;0,600;0,700;1,700&display=swap" rel="stylesheet">
<style>
:root{
  --teal:#17a3b7;
  --teal-dark:#0f8496;
  --green:#8cc63f;
  --ink:#2b3a4a;
  --text:#333;
  --muted:#666;
  --nav:#555b60;
  --soft:#ececec;
  --footer:#262626;
  --white:#fff;
}
*{box-sizing:border-box;margin:0;padding:0}
html,body{width:1200px;height:3974px;overflow:hidden;background:var(--white)}
body{position:relative;font-family:"Open Sans",Arial,sans-serif;color:var(--text)}
.abs{position:absolute}

/* header */
.topbar{left:740px;top:0;width:447px;height:40px;background:var(--teal);color:var(--white);font-size:13px;font-weight:600;display:flex;align-items:center;justify-content:flex-end;gap:22px;padding-right:16px}
.topbar span{display:flex;align-items:center;gap:6px}
.brand{left:44px;top:44px;display:flex;align-items:center;gap:14px}
.brand-mark{width:56px;height:56px;background:var(--teal)}
.brand-name{font-family:"Montserrat",Arial,sans-serif;font-weight:700;font-size:34px;letter-spacing:1px;color:var(--ink);line-height:1}
.search{left:910px;top:88px;width:245px;height:36px;border:1px solid #999;font-size:13px;color:#444;display:flex;align-items:center;justify-content:space-between;padding:0 10px}

/* nav */
.nav{left:13px;top:164px;width:1174px;height:42px;background:var(--nav);display:flex;align-items:center;padding-left:134px;gap:54px;font-family:"Montserrat",Arial,sans-serif;font-weight:600;font-size:13px;color:var(--white);letter-spacing:.5px}
.nav .home{width:50px;height:42px;background:var(--teal);display:flex;align-items:center;justify-content:center;margin-right:-8px}

/* hero */
.hero{left:13px;top:206px;width:1174px;height:662px;background:linear-gradient(180deg,#c9d6dc 0%,#9fb0a2 30%,#5e7a48 60%,#3c4e30 100%)}
.slide-arrow{width:46px;height:46px;background:var(--teal);display:flex;align-items:center;justify-content:center}
.hero-caption{left:0;bottom:0;width:1174px;height:148px;background:rgba(30,30,30,.82);text-align:center;color:var(--white)}
.hero-caption h1{font-family:"Montserrat",Arial,sans-serif;font-size:28px;font-weight:700;letter-spacing:1.5px;margin-top:26px}
.hero-caption h1 em{font-style:normal;color:var(--teal)}
.hero-caption p{font-size:16px;line-height:24px;margin:16px auto 0;width:1100px}

/* section headings */
.sec-head{left:0;width:1200px;display:flex;align-items:center;justify-content:center;gap:16px}
.sec-head .rule{width:70px;height:1px;background:#aaa}
.sec-head .mark{width:34px;height:34px;border:3px solid var(--teal)}
.sec-head h2{font-family:"Montserrat",Arial,sans-serif;font-size:26px;font-weight:700;color:#333;letter-spacing:.5px}
.sec-head h2 em{font-style:normal;color:var(--green)}
.sec-head.light .rule{background:rgba(255,255,255,.7)}
.sec-head.light .mark{border-color:var(--white)}
.sec-head.light h2{color:var(--white)}

.btn{background:var(--teal);color:var(--white);font-family:"Montserrat",Arial,sans-serif;font-weight:700;font-size:13px;display:flex;align-items:center;justify-content:center;border-radius:3px;letter-spacing:.5px}

/* about */
.about-copy{left:40px;top:1005px;width:1120px;text-align:center;font-size:14.5px;line-height:23px}

/* people */
.people{left:13px;top:1245px;width:1174px;height:503px;background:var(--soft)}
.person{width:230px;text-align:center}
.person .portrait{width:198px;height:198px;margin:0 auto;border-radius:50%;border:7px solid var(--white);background:radial-gradient(circle at 50% 40%,#d9d4cf,#8d9499);box-shadow:0 1px 3px rgba(0,0,0,.15)}
.person .name{color:var(--teal);font-weight:700;font-size:16px;margin-top:20px}
.person .role{font-weight:600;font-size:15px;margin-top:4px;color:#333}
.person .social{display:flex;justify-content:center;gap:10px;margin-top:16px}
.person .social i{width:14px;height:14px;border-radius:50%;background:#a9a9a9;display:block}

/* services */
.service{width:520px}
.service .icon{width:127px;height:127px;border-radius:50%;border:3px solid var(--teal);display:flex;align-items:center;justify-content:center;flex:none}
.service h3{color:var(--teal);font-size:16px;font-weight:700}
.service p{font-size:14px;line-height:21px;margin-top:4px}

/* projects */
.projects{left:13px;top:2132px;width:1174px;height:490px;background:linear-gradient(100deg,#1b9fb3 0%,#18a2b6 55%,#2d8f86 80%,#1f6f70 100%)}
.project-photo{left:137px;top:130px;width:436px;height:293px;border:8px solid var(--white);background:linear-gradient(180deg,#d7e3ea 0%,#b5c7cf 45%,#6f8a5a 70%,#8a8f86 100%)}
.project-text{left:615px;top:140px;width:460px;color:var(--white)}
.project-text h3{font-family:"Montserrat",Arial,sans-serif;font-size:17px;font-weight:700;letter-spacing:.5px}
.project-text p{font-size:14.5px;line-height:22px;margin-top:6px}

/* approach */
.approach-svg{left:0;top:2700px}
.step{text-align:center}
.step h4{font-family:"Montserrat",Arial,sans-serif;font-size:16px;font-weight:700;letter-spacing:.5px}
.step p{font-size:14px;line-height:20px;margin-top:4px;color:#333}

/* testimonials */
.clients{left:13px;top:3112px;width:1174px;height:425px;background:var(--soft)}
.quote-box{left:240px;top:142px;width:700px;min-height:146px;background:var(--white);border-radius:6px;box-shadow:0 1px 3px rgba(0,0,0,.12);padding:24px 40px 20px 56px;font-size:14px;line-height:22px}
.quote-box::after{content:"";position:absolute;left:40px;bottom:-14px;border-left:14px solid transparent;border-right:14px solid transparent;border-top:14px solid var(--white)}
.qmark{font-family:Georgia,serif;font-size:40px;font-weight:700;color:#333;line-height:1}
.qmark.open{position:absolute;left:18px;top:18px}
.qmark.close{display:inline-block;vertical-align:-18px;margin-left:8px;height:22px;overflow:visible}
.client-name{left:244px;top:318px;font-weight:700;font-style:italic;font-size:16px}
.dots{left:0;top:356px;width:1174px;display:flex;justify-content:center;gap:6px}
.dots i{width:11px;height:11px;border-radius:50%;border:1.5px solid var(--teal);display:block}
.dots i.on{background:var(--teal)}

/* footer */
.footer{left:13px;top:3550px;width:1174px;height:370px;background:linear-gradient(180deg,#1e1e1e,#2f2f2f)}
.foot-brand{left:0;top:36px;width:1174px;display:flex;justify-content:center;align-items:center;gap:14px}
.foot-brand .brand-mark{background:var(--white);width:60px;height:60px}
.foot-brand .brand-name{color:var(--white);font-size:36px}
.foot-col{top:148px;color:var(--white);font-size:12.5px;line-height:17px}
.foot-col h5{color:var(--teal);font-family:"Montserrat",Arial,sans-serif;font-size:14px;font-weight:700;letter-spacing:.5px;margin-bottom:16px}
.contact-row{display:flex;gap:10px;margin-bottom:10px}
.contact-row .ic{width:20px;height:20px;border-radius:50%;border:1.5px solid var(--white);display:flex;align-items:center;justify-content:center;flex:none}
.newsletter{display:flex;margin-top:4px}
.newsletter .field{width:161px;height:37px;background:var(--white);color:#333;font-size:12.5px;display:flex;align-items:center;padding-left:8px}
.newsletter .go{width:90px;height:37px;background:var(--teal);font-family:"Montserrat",Arial,sans-serif;font-weight:700;font-size:13px;display:flex;align-items:center;justify-content:center}
.copyright{left:13px;top:3920px;width:1174px;height:36px;background:var(--teal);color:var(--white);font-size:11px;font-weight:700;display:flex;align-items:center;justify-content:center;letter-spacing:.5px}
</style>
</head>
<body>

<header>
  <div class="abs topbar">
    <span><svg width="13" height="13" viewBox="0 0 24 24"><path fill="#fff" d="M6.6 10.8a15 15 0 0 0 6.6 6.6l2.2-2.2a1 1 0 0 1 1-.25 11.4 11.4 0 0 0 3.6.6 1 1 0 0 1 1 1V20a1 1 0 0 1-1 1A17 17 0 0 1 3 4a1 1 0 0 1 1-1h3.5a1 1 0 0 1 1 1c0 1.25.2 2.45.6 3.6a1 1 0 0 1-.25 1z"/></svg>+1 (555) 014 2290</span>
    <span><svg width="14" height="11" viewBox="0 0 24 18"><rect x="1" y="1" width="22" height="16" fill="none" stroke="#fff" stroke-width="2"/><path d="M1 1l11 9 11-9" fill="none" stroke="#fff" stroke-width="2"/></svg>hello@meridianadvisers.com</span>
  </div>
  <div class="abs brand"><div class="brand-mark"></div><div class="brand-name">MERIDIAN ADVISERS</div></div>
  <div class="abs search">Search Website
    <svg width="16" height="16" viewBox="0 0 24 24"><circle cx="10" cy="10" r="7" fill="none" stroke="#444" stroke-width="2.5"/><path d="M15 15l6 6" stroke="#444" stroke-width="2.5"/></svg>
  </div>
  <nav class="abs nav">
    <span class="home"><svg width="18" height="16" viewBox="0 0 24 20"><path d="M12 1L1 11h3v8h6v-6h4v6h6v-8h3z" fill="#fff"/></svg></span>
    <span>ABOUT</span><span>OUR PEOPLE</span><span>SERVICES</span><span>PROJECTS</span><span>APPROACH</span><span>TESTIMONIALS</span><span>CONTACT</span>
  </nav>
</header>

<section class="abs hero" role="img" aria-label="Photo of tall residential towers covered in green plants against a blue sky">
  <div class="abs slide-arrow" style="left:0;top:226px"><svg width="14" height="20" viewBox="0 0 14 20"><path d="M11 2L3 10l8 8" fill="none" stroke="#fff" stroke-width="3"/></svg></div>
  <div class="abs slide-arrow" style="right:0;top:226px"><svg width="14" height="20" viewBox="0 0 14 20"><path d="M3 2l8 8-8 8" fill="none" stroke="#fff" stroke-width="3"/></svg></div>
  <div class="abs hero-caption">
    <h1>WELCOME TO <em>MERIDIAN ADVISERS</em></h1>
    <p>Our firm specializes in the sale of apartment properties in Southern California. We have a team of researchers, transaction coordinators and marketing personal to support our geographically specialized advisers.</p>
  </div>
</section>

<section class="about">
  <div class="abs sec-head" style="top:922px"><span class="rule"></span><span class="mark"></span><h2>ABOUT <em>US</em></h2><span class="rule"></span></div>
  <p class="abs about-copy">Lorem ipsum dolor sit amet, consectetuer adipiscing elit, sed diam nonummy nibh euismod tincidunt ut laoreet dolore magna aliquam erat volutpat. Ut wisi enim ad minim veniam, quis nostrud exerci tation ullamcorper suscipit lobortis nisl ut aliquip ex ea commodo consequat. Duis autem vel eum iriure dolor in hendrerit in vulputate velit esse molestie consequat, vel illum dolore eu feugiat nulla facilisis at vero eros et accumsan et iusto odio dignissim qui blandit praesent luptatum zzril delenit augue duis dolore te feugait nulla facilisi. Nam liber tempor cum soluta nobis eleifend option congue nihil imperdiet doming id quod mazim placerat facer possim assum.</p>
  <div class="abs btn" style="left:505px;top:1147px;width:190px;height:38px">LEARN MORE</div>
</section>

<section class="abs people">
  <div class="abs sec-head" style="left:-13px;top:53px"><span class="rule"></span><span class="mark"></span><h2>OUR <em>PEOPLE</em></h2><span class="rule"></span></div>
  <svg class="abs" style="left:58px;top:228px" width="20" height="32" viewBox="0 0 20 32"><path d="M16 2L4 16l12 14" fill="none" stroke="#b5b5b5" stroke-width="3"/></svg>
  <svg class="abs" style="left:1096px;top:228px" width="20" height="32" viewBox="0 0 20 32"><path d="M4 2l12 14L4 30" fill="none" stroke="#b5b5b5" stroke-width="3"/></svg>

  <div class="abs person" style="left:125px;top:145px"><div class="portrait" role="img" aria-label="Portrait of Marcus Ellwood"></div><div class="name">Marcus Ellwood</div><div class="role">Founder &amp; CEO</div><div class="social"><i></i><i></i><i></i><i></i></div></div>
  <div class="abs person" style="left:355px;top:145px"><div class="portrait" role="img" aria-label="Portrait of Owen Talbridge"></div><div class="name">Owen Talbridge</div><div class="role">Co-Founder &amp; CFO</div><div class="social"><i></i><i></i><i></i><i></i></div></div>
  <div class="abs person" style="left:584px;top:145px"><div class="portrait" role="img" aria-label="Portrait of Rosa Kinsley"></div><div class="name">Rosa Kinsley</div><div class="role">COO</div><div class="social"><i></i><i></i><i></i><i></i></div></div>
  <div class="abs person" style="left:814px;top:145px"><div class="portrait" role="img" aria-label="Portrait of Hanna Vorell"></div><div class="name">Hanna Vorell</div><div class="role">CTO</div><div class="social"><i></i><i></i><i></i><i></i></div></div>
</section>

<section class="services">
  <div class="abs sec-head" style="top:1810px"><span class="rule"></span><span class="mark"></span><h2 style="color:var(--green)">SERVICES</h2><span class="rule"></span></div>

  <div class="abs service" style="left:48px;top:1882px;display:flex;gap:14px">
    <div class="icon"><svg width="62" height="62" viewBox="0 0 62 62"><rect x="6" y="8" width="50" height="34" rx="3" fill="none" stroke="#17a3b7" stroke-width="4"/><path d="M14 34l10-10 8 6 14-14" fill="none" stroke="#17a3b7" stroke-width="4"/><rect x="22" y="46" width="18" height="4" fill="#17a3b7"/><rect x="14" y="52" width="34" height="4" fill="#17a3b7"/></svg></div>
    <div style="width:375px"><h3>Property Investment Consulting</h3><p>Lorem ipsum dolor sit amet, consectetuer adipiscing elit, sed diam nonummy nibh euismod tincidunt ut laoreet dolore magna aliquam erat volutpat. Ut wisi enim ad minim veniam, quis nostrud exerci tation ullamcorper suscipit lobortis nisl ut aliquip ex ea commodo.</p></div>
  </div>
  <div class="abs btn" style="left:185px;top:2032px;width:188px;height:37px">LEARN MORE</div>

  <div class="abs service" style="left:620px;top:1882px;display:flex;gap:14px">
    <div class="icon"><svg width="62" height="62" viewBox="0 0 62 62"><path d="M8 56V22L31 8l23 14v34z" fill="#17a3b7"/><g fill="#fff"><rect x="16" y="26" width="8" height="7"/><rect x="27" y="26" width="8" height="7"/><rect x="38" y="26" width="8" height="7"/><rect x="16" y="37" width="8" height="7"/><rect x="38" y="37" width="8" height="7"/><rect x="27" y="40" width="8" height="16"/></g></svg></div>
    <div style="width:375px"><h3>Sales of Apartment Properties</h3><p>Lorem ipsum dolor sit amet, consectetuer adipiscing elit, sed diam nonummy nibh euismod tincidunt ut laoreet dolore magna aliquam erat volutpat. Ut wisi enim ad minim veniam, quis nostrud exerci tation ullamcorper suscipit lobortis nisl ut aliquip ex ea commodo.</p></div>
  </div>
  <div class="abs btn" style="left:757px;top:2032px;width:188px;height:37px">LEARN MORE</div>
</section>

<section class="abs projects" aria-label="Recent projects">
  <div class="abs" style="left:700px;top:0;width:474px;height:490px;background:radial-gradient(ellipse at 70% 40%,rgba(120,180,120,.35),rgba(0,0,0,0) 70%)" role="img" aria-label="Soft background of green foliage"></div>
  <div class="abs sec-head light" style="left:-13px;top:56px"><span class="rule"></span><span class="mark"></span><h2>RECENT PROJECTS</h2><span class="rule"></span></div>
  <div class="abs project-photo" role="img" aria-label="Photo of a terraced apartment building planted with greenery"></div>
  <div class="abs project-text">
    <h3>PARKVIEW TERRACE APARTMENT</h3>
    <p>Lorem ipsum dolor sit amet, consectetuer adipiscing elit, sed diam nonummy nibh euismod tincidunt ut laoreet dolore magna aliquam erat volutpat. Ut wisi enim ad minim veniam, quis nostrud exerci tation ullamcorper suscipit lobortis nisl ut aliquip ex ea commodo consequat. Duis autem vel eum iriure dolor in hendrerit in vulputate velit esse molestie consequat, vel illum dolore eu feugiat nulla facilisis at vero eros et accumsan et iusto odio dignissim qui blandit praesent luptatum zzril delenit augue duis dolore te feugait nulla facilisi.</p>
  </div>
  <svg class="abs" style="left:50px;top:262px" width="20" height="32" viewBox="0 0 20 32"><path d="M16 2L4 16l12 14" fill="none" stroke="#fff" stroke-width="4"/></svg>
  <svg class="abs" style="left:1097px;top:262px" width="20" height="32" viewBox="0 0 20 32"><path d="M4 2l12 14L4 30" fill="none" stroke="#fff" stroke-width="4"/></svg>
</section>

<section class="approach">
  <div class="abs sec-head" style="top:2670px"><span class="rule"></span><span class="mark"></span><h2>OUR <em>APPROACH</em></h2><span class="rule"></span></div>
  <svg class="abs approach-svg" width="1200" height="360" viewBox="0 0 1200 360">
    <path d="M193 198H203A140 140 0 0 0 483 198H455A112 112 0 0 1 231 198H193z" fill="#17a3b7"/>
    <path d="M718 198A140 140 0 0 0 998 198H1007V198H970A112 112 0 0 1 746 198z" fill="#17a3b7"/>
    <rect x="970" y="170" width="37" height="28" fill="#17a3b7"/>
    <rect x="193" y="170" width="38" height="28" fill="#17a3b7"/>
    <path d="M442 200A160 160 0 0 1 762 200H732A130 130 0 0 0 472 200z" fill="#8cc63f"/>
    <circle cx="343" cy="198" r="108" fill="#f2f2f2"/>
    <circle cx="858" cy="198" r="108" fill="#f2f2f2"/>
    <circle cx="602" cy="200" r="126" fill="#f2f2f2"/>
  </svg>
  <div class="abs step" style="left:253px;top:2856px;width:180px"><h4 style="color:var(--teal)">CONSULTING</h4><p>Clients approach us with their investment goals</p></div>
  <div class="abs step" style="left:497px;top:2822px;width:210px"><h4 style="color:var(--green)">OUR EXPERTISE</h4><p>We have a team of researchers, transaction coordinators and marketing personal to support our geographically specialized advisers.</p></div>
  <div class="abs step" style="left:768px;top:2836px;width:180px"><h4 style="color:var(--teal)">REACH GOALS</h4><p>We present the ideal solutions and unique way of better helping clients achieving their investment goals.</p></div>
</section>

<section class="abs clients">
  <div class="abs sec-head" style="left:-13px;top:64px"><span class="rule"></span><span class="mark"></span><h2>WHAT CLIENTS <em>SAY</em></h2><span class="rule"></span></div>
  <div class="abs quote-box">
    <span class="qmark open">“</span>
    <p>Lorem ipsum dolor sit amet, consectetuer adipiscing elit, sed diam nonummy nibh euismod tincidunt ut laoreet dolore magna aliquam erat volutpat. Ut wisi enim ad minim veniam, quis nostrud exerci tation ullamcorper suscipit lobortis nisl ut aliquip ex ea commodo conse quat. Duis autem vel eum iriure dolor in hendrerit in vulputate velit esse.<span class="qmark close">”</span></p>
  </div>
  <div class="abs client-name">Peter Lanford</div>
  <div class="abs dots"><i class="on"></i><i></i><i></i><i></i></div>
</section>

<footer class="abs footer">
  <div class="abs foot-brand"><div class="brand-mark"></div><div class="brand-name">MERIDIAN ADVISERS</div></div>

  <div class="abs foot-col" style="left:111px">
    <h5>QUICK LINKS</h5>
    Home<br>About<br>Our People<br>Services<br>Approach<br>Testimonials<br>Contact
  </div>
  <div class="abs foot-col" style="left:284px">
    <h5>SERVICES</h5>
    Property Investment Consulting<br>Sale of Apartment Properties
  </div>
  <div class="abs foot-col" style="left:547px;width:240px">
    <h5>CONTACT</h5>
    <div class="contact-row"><span class="ic"><svg width="10" height="12" viewBox="0 0 10 14"><path d="M5 0a5 5 0 0 0-5 5c0 4 5 9 5 9s5-5 5-9a5 5 0 0 0-5-5zm0 7a2 2 0 1 1 0-4 2 2 0 0 1 0 4z" fill="#fff"/></svg></span><span>Meridian Advisers<br>48 Harbor Vista Rd<br>Suite #210<br>Long Beach, CA 90802</span></div>
    <div class="contact-row"><span class="ic"><svg width="10" height="10" viewBox="0 0 24 24"><path fill="#fff" d="M6.6 10.8a15 15 0 0 0 6.6 6.6l2.2-2.2a1 1 0 0 1 1-.25 11.4 11.4 0 0 0 3.6.6 1 1 0 0 1 1 1V20a1 1 0 0 1-1 1A17 17 0 0 1 3 4a1 1 0 0 1 1-1h3.5a1 1 0 0 1 1 1c0 1.25.2 2.45.6 3.6a1 1 0 0 1-.25 1z"/></svg></span><span style="line-height:20px">+1 (555) 014 2290</span></div>
    <div class="contact-row"><span class="ic"><svg width="10" height="8" viewBox="0 0 24 18"><rect x="1" y="1" width="22" height="16" fill="none" stroke="#fff" stroke-width="3"/><path d="M1 1l11 9 11-9" fill="none" stroke="#fff" stroke-width="3"/></svg></span><span style="line-height:20px">hello@meridianadvisers.com</span></div>
  </div>
  <div class="abs foot-col" style="left:811px">
    <h5>NEWSLETTER SIGN UP</h5>
    <div class="newsletter"><div class="field">Enter Email Address</div><div class="go">SIGN UP</div></div>
  </div>
</footer>
<div class="abs copyright">© COPYRIGHT 2017 MERIDIAN ADVISERS. ALL RIGHTS RESERVED</div>

</body>
</html>
```